Brightwave Business Card

Professional Business Card Design required using the attached contact information.

Contact information can be rearranged as required.

The company is a new start up venture developing solar systems, the branding should be in keeping with that of one of the investors whose website is as follows https://www.quorvex.com/

```html
<!DOCTYPE html>
<html lang="en">
<head>
<meta charset="utf-8">
<title>Brightwave Renewables – Business Card</title>
<link rel="stylesheet" href="https://fonts.googleapis.com/css2?family=Montserrat:wght@400;600;700&family=Roboto:wght@400&display=swap">
<style>
  :root {
    --bg: #e4e4e4;
    --card-dark-a: #2b3039;
    --card-dark-b: #434955;
    --card-light: #ffffff;
    --ink: #1f2227;
    --ink-soft: #3a3d42;
    --accent: #2e6b55;
    --rule: #2a2d31;
    --white: #ffffff;
  }
  * { box-sizing: border-box; margin: 0; padding: 0; }
  html, body { width: 1200px; height: 900px; overflow: hidden; }
  body {
    background: var(--bg);
    position: relative;
    font-family: "Roboto", sans-serif;
  }
  .card {
    position: absolute;
    left: 300px;
    width: 600px;
    height: 343px;
    border-radius: 18px;
    box-shadow: 0 10px 24px rgba(0,0,0,0.18);
    overflow: hidden;
  }
  .card--back {
    top: 90px;
    background: linear-gradient(120deg, var(--card-dark-a) 0%, var(--card-dark-b) 45%, var(--card-dark-a) 100%);
    display: flex;
    align-items: center;
    justify-content: center;
  }
  .card--front {
    top: 473px;
    background: var(--card-light);
  }
  .wordmark {
    font-family: "Montserrat", sans-serif;
    font-weight: 600;
    white-space: nowrap;
    display: flex;
    align-items: center;
    gap: 12px;
  }
  .wordmark__dot {
    border-radius: 50%;
    flex: none;
  }
  .card--back .wordmark { color: var(--white); font-size: 32px; }
  .card--back .wordmark__dot { width: 22px; height: 22px; background: var(--white); }
  .card--front .wordmark {
    position: absolute;
    top: 36px; right: 40px;
    color: var(--ink);
    font-size: 24px;
  }
  .card--front .wordmark__dot { width: 18px; height: 18px; background: var(--accent); }
  .holder {
    position: absolute;
    left: 44px;
    top: 100px;
  }
  .holder__name {
    font-family: "Montserrat", sans-serif;
    font-weight: 700;
    font-size: 25px;
    line-height: 1.2;
    color: var(--ink-soft);
  }
  .holder__title {
    font-family: "Montserrat", sans-serif;
    font-weight: 400;
    font-size: 15px;
    color: var(--accent);
    margin-top: 2px;
  }
  .holder__rule {
    width: 40px; height: 2px;
    background: var(--rule);
    margin: 10px 0 14px;
  }
  .address {
    font-size: 14.5px;
    line-height: 1.3;
    color: var(--ink-soft);
    font-style: normal;
  }
  .contacts {
    list-style: none;
    margin-top: 12px;
    font-size: 14.5px;
    color: var(--ink-soft);
  }
  .contacts li {
    display: flex;
    align-items: center;
    gap: 8px;
    line-height: 1.35;
  }
  .contacts svg { width: 13px; height: 13px; fill: var(--ink-soft); flex: none; }
</style>
</head>
<body>
  <section class="card card--back" aria-label="Card back">
    <div class="wordmark"><span class="wordmark__dot"></span><span>Brightwave Renewables</span></div>
  </section>

  <section class="card card--front" aria-label="Card front">
    <div class="wordmark"><span class="wordmark__dot"></span><span>Brightwave Renewables</span></div>

    <div class="holder">
      <h1 class="holder__name">Daniel Harrow</h1>
      <p class="holder__title">Director</p>
      <div class="holder__rule"></div>
      <address class="address">
        Brightwave Renewables LLC<br>
        318 Harbor Street,<br>
        Portland, ME 04101
      </address>
      <ul class="contacts">
        <li>
          <svg viewBox="0 0 24 24" aria-hidden="true"><path d="M6.6 10.8a15.1 15.1 0 0 0 6.6 6.6l2.2-2.2a1 1 0 0 1 1-.25 11.4 11.4 0 0 0 3.6.57 1 1 0 0 1 1 1V20a1 1 0 0 1-1 1A17 17 0 0 1 3 4a1 1 0 0 1 1-1h3.5a1 1 0 0 1 1 1c0 1.25.2 2.45.57 3.6a1 1 0 0 1-.25 1z"/></svg>
          <span>+1 (555) 014-2276</span>
        </li>
        <li>
          <svg viewBox="0 0 24 24" aria-hidden="true"><path d="M2 5h20v14H2zm2 2v.5l8 5 8-5V7l-8 5z"/></svg>
          <span>daniel.harrow@brightwave-renewables.com</span>
        </li>
        <li>
          <svg viewBox="0 0 24 24" aria-hidden="true"><circle cx="12" cy="12" r="10"/></svg>
          <span>www.brightwave-renewables.com</span>
        </li>
      </ul>
    </div>
  </section>
</body>
</html>
```